Commercial janitorial cleaning

Janitorial cleaning particularly for commercial buildings. Website needs to specify free estimates. Location of service is Hudson, Valatie, East Greenbush, Troy, Albany ny area. Services page with Janitorial services- General Office Cleaning, Construction Cleaning, Carpet Extraction, Consultation/Business, Lighting Maintenance, Seasonal Deep Cleaning, Window cleaning, Event Cleaning, Floor and Carpet Cleaning, Floor Striping and Waxing. Contact us page with email phone number on page and a request page that emails me if they have any questions. About us page-the picture of my family on it with a section I can type a story myself.

Target Market(s)

Commercial businesses

Industry/Entity Type

Janitorial Service

Number of Pages Required

4 page

Font styles to use
Serif
Sans Serif
Script

Colors
ec1f27
1b1b1b
ffffff
9d9d9d

Requirements
Must have
• Phone number 555-314-2760. Must have free estimates on home page. Going for industrial / modern look to website
Nice to have
• Logo is a red and black building so if those colors could be coordinated to website that would be awesome.

```html
<!DOCTYPE html>
<html lang="en">
<head>
<meta charset="utf-8">
<title>Brightwing Cleaning Services</title>
<link href="https://fonts.googleapis.com/css2?family=Roboto:wght@400;500;700;900&family=Lato:wght@400;700&display=swap" rel="stylesheet">
<style>
:root{
  --red:#ec1f27;
  --ink:#1b1b1b;
  --white:#ffffff;
  --grey:#9d9d9d;
  --light:#f0f0f0;
  --body:#333333;
}
*{margin:0;padding:0;box-sizing:border-box}
html,body{width:1200px;height:2378px;overflow:hidden;background:var(--white)}
body{position:relative;font-family:"Lato",sans-serif;color:var(--ink)}
.abs{position:absolute}

/* header */
.site-header{position:absolute;left:0;top:0;width:1200px;height:140px;border-top:2px solid var(--ink);background:var(--white)}
.brand{position:absolute;left:160px;top:30px;width:150px;text-align:center;font-family:"Roboto",sans-serif;font-weight:700;font-size:16px;line-height:18px;color:var(--ink)}
.brand-mark{display:block;width:40px;height:40px;background:var(--red);margin:0 auto 10px}
.contact-item{position:absolute;top:14px;display:flex;align-items:flex-start;gap:10px;font-family:"Lato",sans-serif;font-size:13px;line-height:17px;color:var(--ink)}
.contact-item svg{flex:none}
.cta-top{position:absolute;left:888px;top:14px;width:152px;height:30px;background:var(--red);color:var(--white);font-family:"Roboto",sans-serif;font-weight:700;font-size:15px;line-height:30px;text-align:center;clip-path:polygon(0 0,100% 0,100% 70%,94% 100%,0 100%)}
.main-nav{position:absolute;left:480px;top:92px;width:560px;height:40px}
.main-nav a{position:absolute;top:0;width:100px;text-align:center;font-family:"Lato",sans-serif;font-size:13px;color:var(--ink);text-decoration:none}
.main-nav a svg{display:block;margin:0 auto 4px}
.main-nav a.is-active{color:var(--red)}

/* hero */
.hero{position:absolute;left:0;top:140px;width:1200px;height:437px;background:linear-gradient(120deg,#7a0d10 0%,#d81c24 35%,#f2a7b5 60%,#e8c4e0 75%,#e3242b 100%)}
.hero-arrow{position:absolute;top:200px;width:30px;height:38px;background:rgba(60,60,60,.6)}
.hero-box{position:absolute;left:740px;top:100px;width:305px;height:235px;background:rgba(27,27,27,.88);border:2px solid rgba(255,255,255,.25);color:var(--white);text-align:center}
.hero-box h1{font-family:"Roboto",sans-serif;font-weight:700;font-size:20px;line-height:29px;text-transform:uppercase;margin-top:22px}
.hero-box p{font-family:"Lato",sans-serif;font-size:21px;line-height:30px;margin-top:18px}

/* welcome */
.welcome-title{position:absolute;left:163px;top:628px;font-family:"Roboto",sans-serif;font-weight:900;font-size:34px;line-height:40px;color:var(--ink)}
.welcome-title span{color:var(--red);display:block}
.welcome-rule{position:absolute;left:160px;top:733px;width:512px;height:1px;background:#dcdcdc}
.welcome-text{position:absolute;left:160px;top:748px;width:515px;font-size:12.3px;line-height:21.5px;color:var(--body)}
.team-photo{position:absolute;left:735px;top:622px;width:445px;height:331px;background:radial-gradient(ellipse at 50% 60%,#f4d9a8 0%,#e9e3dc 45%,#ffffff 80%)}

/* band */
.band{position:absolute;left:0;top:953px;width:1200px;height:301px;background:linear-gradient(90deg,#262626,#3c3c3c 50%,#2a2a2a)}
.band p{position:absolute;left:250px;top:56px;width:700px;text-align:center;color:var(--white);font-family:"Lato",sans-serif;font-weight:700;font-size:23px;line-height:31px}
.band-btn{position:absolute;left:440px;top:168px;width:320px;height:58px;background:var(--red);color:var(--white);font-family:"Lato",sans-serif;font-weight:700;font-size:23px;line-height:58px;text-align:center;clip-path:polygon(4% 0,100% 0,100% 75%,96% 100%,0 100%,0 25%)}

/* services */
.services{position:absolute;left:0;top:1254px;width:1200px;height:656px;background:var(--light)}
.section-title{position:absolute;left:0;width:1200px;text-align:center;font-family:"Roboto",sans-serif;font-weight:900;font-size:34px;color:var(--ink)}
.section-title span{color:var(--red)}
.section-rule{position:absolute;left:408px;width:384px;height:1px;background:#d0d0d0}
.section-badge{position:absolute;left:590px;width:20px;height:22px;background:var(--red);outline:6px solid var(--light)}
.hub{position:absolute;left:450px;top:1543px;width:300px;height:300px;border-radius:50%;background:var(--white);border:8px solid #e4e4e4;display:flex;flex-direction:column;align-items:center;justify-content:center;font-family:"Roboto",sans-serif;font-weight:700;font-size:26px;line-height:30px;text-align:center;color:var(--ink)}
.hub i{display:block;width:22px;height:22px;background:var(--red);margin-bottom:14px}
.svc{position:absolute;font-size:15.5px;color:var(--ink);white-space:nowrap}
.svc.left{text-align:right}
.svc.is-active{color:var(--red)}
.svc-icon{position:absolute;width:52px;height:50px;background:var(--ink);border:3px solid var(--white);box-shadow:0 0 0 1px #cfcfcf;clip-path:polygon(0 0,78% 0,100% 22%,100% 100%,22% 100%,0 78%)}
.svc-icon.is-active{background:var(--red)}
.svc-icon::after{content:"";position:absolute;left:15px;top:14px;width:16px;height:16px;border:2px solid var(--white);border-radius:3px}

/* testimonials */
.testimonial{position:absolute;top:2082px}
.avatar{position:absolute;width:90px;height:74px;background:linear-gradient(160deg,#8a6a52,#c9b7a4);border:3px solid var(--white);outline:2px solid var(--red)}
.quote{position:absolute;width:305px;height:112px;background:#ececec;padding:16px 22px;font-size:12px;line-height:17px;color:#555}
.quote b{display:block;margin-top:10px;font-size:11px;color:var(--ink);font-weight:700}
.t-arrow{position:absolute;top:2120px}

/* footer */
.site-footer{position:absolute;left:0;top:2258px;width:1200px;height:120px;background:#111}
.footer-nav a{position:absolute;top:33px;font-size:12px;color:var(--white);text-decoration:none}
.footer-nav a.is-active{color:var(--red)}
.footer-badge{position:absolute;left:546px;top:-36px;width:68px;height:70px;background:var(--white);border:4px solid var(--red);display:flex;align-items:center;justify-content:center}
.footer-badge i{width:26px;height:26px;background:var(--red)}
.footer-rule{position:absolute;left:160px;top:66px;width:880px;height:1px;background:#333}
.copyright{position:absolute;left:163px;top:90px;font-size:11px;color:var(--white)}
.social{position:absolute;top:83px;width:26px;height:26px;background:var(--red);border-radius:4px}
</style>
</head>
<body>

<header class="site-header">
  <div class="brand"><span class="brand-mark"></span>Brightwing<br>Cleaning Services</div>

  <div class="contact-item" style="left:512px">
    <svg width="30" height="32" viewBox="0 0 30 32"><circle cx="15" cy="16" r="13" fill="none" stroke="#ec1f27" stroke-width="2"/><path d="M10 9c1-1 3 0 3 2l-1 2c1 2 2 4 4 5l2-1c2 0 3 2 2 3l-2 2c-5 0-10-6-10-11z" fill="#ec1f27"/></svg>
    <div>Call Us:<br>555-314-2760</div>
  </div>
  <div class="contact-item" style="left:642px">
    <svg width="32" height="30" viewBox="0 0 32 30"><path d="M2 10l14-8 14 8v18H2z" fill="none" stroke="#ec1f27" stroke-width="2"/><path d="M2 10l14 10 14-10" fill="none" stroke="#ec1f27" stroke-width="2"/></svg>
    <div>Mail Us:<br>info@brightwingcleaning.com</div>
  </div>
  <div class="cta-top">Free Estimates</div>

  <nav class="main-nav">
    <a href="#" class="is-active" style="left:0"><svg width="16" height="14" viewBox="0 0 16 14"><path d="M8 0l8 7h-2v7h-4v-4H6v4H2V7H0z" fill="#ec1f27"/></svg>Home</a>
    <a href="#" style="left:154px"><svg width="16" height="14" viewBox="0 0 16 14"><circle cx="5" cy="4" r="3" fill="#1b1b1b"/><circle cx="11" cy="4" r="3" fill="#1b1b1b"/><path d="M0 14c0-4 2-6 5-6s5 2 5 6zM7 14c0-4 2-6 4-6s5 2 5 6z" fill="#1b1b1b"/></svg>About</a>
    <a href="#" style="left:315px"><svg width="16" height="14" viewBox="0 0 16 14"><path d="M2 12l5-5 3 3-5 5zM8 6l3-5 4 4-5 3z" fill="#1b1b1b"/></svg>Services</a>
    <a href="#" style="left:470px"><svg width="16" height="14" viewBox="0 0 16 14"><rect x="1" y="2" width="11" height="11" fill="none" stroke="#1b1b1b" stroke-width="2"/><path d="M6 9l8-8 2 2-8 8H6z" fill="#1b1b1b"/></svg>Contact</a>
  </nav>
</header>

<section class="hero" role="img" aria-label="Red-tinted photo of a modern glass office tower seen from below">
  <div class="hero-arrow" style="left:0"></div>
  <div class="hero-box">
    <h1>We Offer Janitorial<br>Cleaning Particularly<br>For Commercial<br>Buildings</h1>
    <p>Serving All of Hudson,<br>Valatie, Troy &amp; Albany</p>
  </div>
</section>

<h2 class="welcome-title">Welcome To<span>Brightwing Cleaning Services</span></h2>
<div class="welcome-rule"></div>
<p class="welcome-text">Lorem ipsum dolor sit amet, consectetuer adipiscing elit, sed diam nonummy nibh euismod tincidunt ut laoreet dolore magna aliquam erat volutpat. Ut wisi enim ad minim veniam, quis nostrud exerci tation ullamcorper suscipit lobortis nisl ut aliquip ex ea commodo consequat. Duis autem vel eum iriure dolor in hendrerit in vulputate velit esse molestie consequat, vel illum dolore eu feugiat nulla facilisis at vero eros et accumsan et iusto odio dignissim qui blandit praesent luptatum zzril delenit augue duis dolore te feugait nulla facilisi.</p>
<div class="team-photo" role="img" aria-label="Photo of three smiling cleaning staff holding buckets of supplies beside yellow mop carts"></div>

<section class="band" role="img" aria-label="Dark photo of a worker polishing a tile floor with a buffing machine">
  <p>Providing A Full Line Of Janitorial Services Including Tile Floor Waxing/stripping, Carpet Cleaning Services, Emergency Water Extractions, And More.</p>
  <div class="band-btn">Request Free A Estimates</div>
</section>

<section class="services" role="img" aria-label="Faint background photo of cleaning supplies and brushes"></section>
<h2 class="section-title" style="top:1306px">Our <span>Services</span></h2>
<div class="section-rule" style="top:1380px"></div>
<div class="section-badge" style="top:1370px"></div>

<div class="hub"><i></i>Brightwing<br>Cleaning Services</div>

<div class="svc-icon is-active" style="left:450px;top:1422px"></div>
<div class="svc left is-active" style="right:771px;top:1438px">General Office Cleaning</div>
<div class="svc-icon" style="left:365px;top:1514px"></div>
<div class="svc left" style="right:852px;top:1530px">Construction Cleaning</div>
<div class="svc-icon" style="left:352px;top:1608px"></div>
<div class="svc left" style="right:866px;top:1624px">Carpet Extraction</div>
<div class="svc-icon" style="left:365px;top:1701px"></div>
<div class="svc left" style="right:852px;top:1717px">Consultation/Business</div>
<div class="svc-icon" style="left:450px;top:1793px"></div>
<div class="svc left" style="right:770px;top:1809px">Lighting Maintenance</div>

<div class="svc-icon" style="left:690px;top:1422px"></div>
<div class="svc" style="left:768px;top:1438px">Seasonal Deep Cleaning</div>
<div class="svc-icon" style="left:775px;top:1514px"></div>
<div class="svc" style="left:852px;top:1530px">Floor and Carpet Cleaning</div>
<div class="svc-icon" style="left:790px;top:1608px"></div>
<div class="svc" style="left:866px;top:1624px">Event Cleaning,</div>
<div class="svc-icon" style="left:775px;top:1701px"></div>
<div class="svc" style="left:850px;top:1717px">Window Cleaning</div>
<div class="svc-icon" style="left:690px;top:1793px"></div>
<div class="svc" style="left:770px;top:1809px">Floor Striping and Waxing</div>

<h2 class="section-title" style="top:1962px">Client <span>Testimonials</span></h2>
<div class="section-rule" style="top:2035px"></div>
<div class="section-badge" style="top:2025px"></div>

<svg class="t-arrow" style="left:130px" width="14" height="40" viewBox="0 0 14 40"><path d="M12 2L2 20l10 18" fill="none" stroke="#c8c8c8" stroke-width="2"/></svg>
<svg class="t-arrow" style="left:1056px" width="14" height="40" viewBox="0 0 14 40"><path d="M2 2l10 18L2 38" fill="none" stroke="#ec1f27" stroke-width="2"/></svg>

<div class="avatar" style="left:165px;top:2104px" role="img" aria-label="Client portrait photo"></div>
<div class="quote" style="left:273px;top:2083px">"Ut wisi enim ad minim veniam, quis nostrud exerci tation ullamcorper suscipit lobortis nisl ut aliquip ex ea commodo consequat uis autem vel eum.<b>DANA WHITCOMB</b></div>
<div class="avatar" style="left:624px;top:2104px" role="img" aria-label="Client portrait photo"></div>
<div class="quote" style="left:732px;top:2083px">"Ut wisi enim ad minim veniam, quis nostrud exerci tation ullamcorper suscipit lobortis nisl ut aliquip ex ea commodo consequat uis autem vel eum.<b>PRIYA CASTELL</b></div>

<footer class="site-footer">
  <div class="footer-badge"><i></i></div>
  <nav class="footer-nav">
    <a href="#" class="is-active" style="left:300px">Home</a>
    <a href="#" style="left:423px">About</a>
    <a href="#" style="left:710px">Services</a>
    <a href="#" style="left:852px">Contact</a>
  </nav>
  <div class="footer-rule"></div>
  <p class="copyright">Copyright © 2017 Brightwing Cleaning Services. All Right Reserved.</p>
  <span class="social" style="left:897px"></span>
  <span class="social" style="left:934px"></span>
  <span class="social" style="left:971px"></span>
  <span class="social" style="left:1008px"></span>
</footer>

</body>
</html>
```